Online only (mobile devices) 50th Birthday Invitation

Design an online (surprise) 50th Birthday dinner invitation for a female (Gwendolyn). It should be elegant and similar to the examples uploaded. Will provide restaurant address details, times and RSVP details to winning designer. Please mock up.
Details should be:
Saturday 12th April 2025
Arrive between 6:30pm and 6:45pm
Restaurant Name
Restaurant Address
RSVP name and mobile phone by Friday 4 April 2025
Target Market(s)
The person's friends and family
Requirements
Must have
- Elegance and class
Nice to have
- Gold or silver colouring

```html
<!DOCTYPE html>
<html lang="en">
<head>
<meta charset="UTF-8">
<title>Gwendolyn's Fabulous Fifty</title>
<link rel="stylesheet" href="https://fonts.googleapis.com/css2?family=Antonio:wght@300&family=Kaushan+Script&family=Montserrat:wght@400&display=swap">
<style>
  :root {
    --ink: #202022;
    --gold: #b8954f;
    --cream: #fbf8ef;
  }
  html, body {
    margin: 0;
    padding: 0;
    overflow: hidden;
    background: var(--ink);
  }
  .invitation {
    position: relative;
    width: 851px;
    height: 1200px;
    background: var(--ink);
    overflow: hidden;
    color: var(--cream);
  }
  .invitation p { margin: 0; position: absolute; left: 80px; white-space: nowrap; }
  .intro {
    top: 180px;
    font-family: "Montserrat", sans-serif;
    font-size: 22px;
    letter-spacing: 2.6px;
  }
  .honoree {
    top: 228px;
    font-family: "Antonio", sans-serif;
    font-weight: 300;
    font-size: 57px;
    letter-spacing: 5px;
    line-height: 1;
  }
  .headline {
    font-family: "Kaushan Script", cursive;
    color: var(--gold);
    line-height: 1;
  }
  .headline-first { top: 340px; left: 58px !important; font-size: 158px; }
  .headline-second { top: 530px; left: 74px !important; font-size: 158px; }
  .event-when {
    top: 852px;
    font-family: "Antonio", sans-serif;
    font-weight: 300;
    font-size: 41px;
    letter-spacing: 4px;
    line-height: 1;
  }
  .venue, .address, .rsvp {
    font-family: "Montserrat", sans-serif;
    font-size: 20px;
    letter-spacing: 2.4px;
  }
  .venue { top: 914px; }
  .address { top: 953px; }
  .rsvp { top: 1086px; letter-spacing: 2.6px; }
  .brush-pattern {
    position: absolute;
    top: 0;
    left: 694px;
    width: 157px;
    height: 1200px;
  }
</style>
</head>
<body>
  <main class="invitation">
    <p class="intro">Come and celebrate with us!</p>
    <p class="honoree">GWENDOLYN IS TURNING</p>
    <p class="headline headline-first">Fabulous</p>
    <p class="headline headline-second">Fifty</p>
    <p class="event-when">04.12.25 | SAT | 6.30 PM</p>
    <p class="venue">The Larkmoor Hotel</p>
    <p class="address">4178 Alder Crest Ave. Brookhaven, NY</p>
    <p class="rsvp">RSVP your Name by Friday 4 April 2025</p>
    <svg class="brush-pattern" role="img" aria-label="Decorative column of gold and cream brush strokes" viewBox="0 0 157 1200" preserveAspectRatio="none">
      <defs>
        <linearGradient id="strokeTone" x1="0" y1="0" x2="1" y2="1">
          <stop offset="0" stop-color="#6e5c3a"/>
          <stop offset="0.5" stop-color="#8a7a5c"/>
          <stop offset="1" stop-color="#6e5c3a"/>
        </linearGradient>
      </defs>
      <rect width="157" height="1200" fill="url(#strokeTone)" opacity="0.55"/>
    </svg>
  </main>
</body>
</html>
```